Bref créative
Bath/Spa Product Label
Vesta Reef
Thanks to you expert graphic artists we have been happy with the logo designed last summer and would like to see what you wizards can do to with a product label.
We have attached the current logo and would love to see what you can do with creating a product label that will fit several types of labels.
1. We need a vertical orientation of the label to be scalable so that we can use it on 16 oz or 8 ounce bottles.
2. We need a horizontal orientation that is also scalable for 8 ounce or 4 ounce jars.
You can place the uploaded logo anywhere on the labels but we need blank space to fill in the product name, net weight, instructions and ingredients.
Feel free to apply generic text for the net weight, instructions and ingredients. We manufacture shampoos, conditioners, body washes, shower gels, body scrubs, foot scrubs, sugar scrubs, etc.
We have attached two sample MS Word documents with the ugly and boring labels we use now. Use these as inspiration to move us to the next level. Go ahead add color, fonts, additional graphics - whatever you see fit. In the past, we have treated our designers fairly and cordially. You can expect the same treatment for this contest.
Personal Care
Over 95% of our customer base is women. But keep in mind that men also use shower gels - so no teddy bears on the product label please.Our clients are used to high quality product, not over hyped claims or garish designs.
As stated above we need the label in at least two orientations. It must also be scalable so that we can use it on different size labels. If you can design a third label in square dimensions that would be a big bonus.
Current jar label - for example DO NOT REPLICATE.
Sample shampoo/body wash label applied vertically to 16 ounce or 8 ounce bottles. FOR EXAMPLE ONLY DO NOT REPLICATE
Current logo - DO NOT DISTRIBUTE - COPYRIGHT VESTA REEF.

```html
<!DOCTYPE html>
<html lang="en">
<head>
<meta charset="utf-8">
<title>Vesta Reef – Glistening Sugar Scrub Jar Label</title>
<link rel="stylesheet" href="https://fonts.googleapis.com/css2?family=Cinzel:wght@400&family=Cormorant+Garamond:ital,wght@1,500&family=Open+Sans:wght@400&display=swap">
<style>
  :root {
    --stage: #6a6a6a;
    --violet-deep: #3f2c82;
    --violet: #5a45a8;
    --violet-light: #7c6cc4;
    --magenta: #9a4aa6;
    --cream: #fffbea;
    --cream-mid: #fbeec2;
    --cream-warm: #f4d488;
    --gold: #c99a3e;
    --gold-soft: rgba(201, 154, 62, 0.35);
    --ink-violet: #4b3a93;
    --ink: #2c2440;
    --panel-white: rgba(255, 255, 255, 0.84);
  }
  * { box-sizing: border-box; margin: 0; padding: 0; }
  html, body { width: 1200px; height: 850px; overflow: hidden; }
  body {
    background: var(--stage);
    position: relative;
    font-family: "Open Sans", sans-serif;
  }
  .jar-label {
    position: absolute;
    left: 40px;
    top: 292px;
    width: 1120px;
    height: 266px;
    overflow: hidden;
    box-shadow: 0 4px 14px rgba(0, 0, 0, 0.35);
  }
  .swirl-field {
    position: absolute; inset: 0;
    background:
      radial-gradient(ellipse 60% 80% at 18% 85%, rgba(154, 74, 166, 0.55), transparent 70%),
      radial-gradient(ellipse 50% 70% at 85% 30%, rgba(154, 74, 166, 0.5), transparent 70%),
      linear-gradient(120deg, var(--violet-light) 0%, var(--violet-deep) 45%, var(--violet) 100%);
  }
  .centre-art { position: absolute; inset: 0; width: 100%; height: 100%; }
  .info-box {
    position: absolute;
    background: var(--panel-white);
    color: var(--ink);
  }
  .info-box--description {
    left: 21px; top: 27px; width: 380px; height: 213px;
    padding: 18px 22px;
    font-size: 17px; line-height: 1.45;
  }
  .net-weight {
    position: absolute; left: 40px; bottom: 16px;
    font-size: 15px;
  }
  .info-box--ingredients {
    left: 755px; top: 24px; width: 345px; height: 184px;
    padding: 12px 16px;
    font-size: 12px; line-height: 1.5;
  }
  .warning { margin-top: 14px; }
  .brand-block {
    position: absolute;
    left: 380px; width: 360px; top: 0; height: 266px;
    text-align: center;
  }
  .brand-flourish {
    position: absolute; left: 40px; top: 18px; width: 280px; height: 92px;
    border-radius: 50%;
    background: radial-gradient(ellipse at center, var(--gold-soft), rgba(201,154,62,0.12) 55%, rgba(201,154,62,0) 75%);
  }
  .brand-name {
    position: absolute; left: 0; right: 0; top: 106px;
    display: flex; align-items: center; justify-content: center; gap: 12px;
    font-family: "Cinzel", serif;
    font-weight: 400;
    font-size: 36px;
    line-height: 1;
    letter-spacing: 1px;
    color: var(--ink-violet);
  }
  .brand-mark {
    width: 26px; height: 26px; border-radius: 50%;
    background: var(--gold);
    flex: none;
  }
  .product-name {
    position: absolute; left: 28px; right: 28px; top: 168px;
    font-family: "Cormorant Garamond", serif;
    font-style: italic; font-weight: 500;
    font-size: 21px; line-height: 1.4;
    color: var(--ink-violet);
  }
</style>
</head>
<body>
  <section class="jar-label" aria-label="Sugar scrub jar label">
    <div class="swirl-field" role="img" aria-label="Violet and magenta decorative swirl pattern"></div>
    <svg class="centre-art" viewBox="0 0 1120 266" preserveAspectRatio="none" aria-hidden="true">
      <defs>
        <radialGradient id="creamGlow" cx="0.5" cy="0.45" r="0.7">
          <stop offset="0" stop-color="#fffbea"/>
          <stop offset="0.6" stop-color="#fbeec2"/>
          <stop offset="1" stop-color="#f4d488"/>
        </radialGradient>
      </defs>
      <path class="centre-panel" fill="url(#creamGlow)" stroke="#c99a3e" stroke-width="2"
        d="M370 0 H750 C720 45 765 95 735 133 C765 171 720 221 750 266 H370 C400 221 355 171 385 133 C355 95 400 45 370 0 Z"/>
    </svg>

    <div class="info-box info-box--description">
      <p>A unique blend of safflower oil, sugar and Jojoba beads, to exfoliate and bring a lovely glow to your skin. Scented with invigorating Lavender Mint.</p>
      <p class="net-weight">150 gram</p>
    </div>

    <div class="brand-block">
      <div class="brand-flourish" role="img" aria-label="Soft gold glow with decorative flourish above the brand name"></div>
      <h1 class="brand-name"><span class="brand-mark" aria-hidden="true"></span>VESTA REEF</h1>
      <p class="product-name">Glistening Sugar Scrub with Jojoba Beads and Lavender Mint Scent</p>
    </div>

    <div class="info-box info-box--ingredients">
      <p>Ingredients: Sucrose, Carthamus tinctorius (Safflower) Seed Oil, Polyethylene, Tocopherol Acetate (Vitamin E), Fragrance, Silica, Phenoxyethanol</p>
      <p class="warning">WARNING: This product contains natural oils that can make surfaces slippery. Use caution whenever using this product to prevent possible injury.</p>
    </div>
  </section>
</body>
</html>
```